New Look for Existing Website
Keep it simple, clean, crisp & clear
Creative Brief
Automotive
www.bitlocate.ie
We are an advertising website where people search for and view lists of results and associated information for second hand car parts suppliers.
we like Zorvane for its simplicity. We like clean and simple websites, easy to navigate and not cluttered with lots of links/advertisements or too much text.
www.zorvane.ie
http://www.klimbrook.ie/klimbrook/publish/vehicleLookup.jsp
please view the existing website at www.bitlocate.ie and then create new look for the main page/template every are should have its own box/ container with soft borders also logo looks too plain and can be changed if required.

```html
<!DOCTYPE html>
<html lang="en">
<head>
<meta charset="utf-8">
<title>BitLocate.ie – Car Dismantlers &amp; Car Parts Search</title>
<link href="https://fonts.googleapis.com/css2?family=Arimo:wght@400;700&display=swap" rel="stylesheet">
<style>
  :root {
    --ink: #111111;
    --muted: #777777;
    --rule: #d6d6d6;
    --panel-border: #d2d2d2;
    --field-bg: #bfbfbf;
    --field-text: #f4f4f4;
    --button-bg: #bfe0f2;
    --button-border: #6fb6dd;
    --button-text: #1e6fa3;
    --link-blue: #1e88c7;
    --ad-red: #d9261c;
    --ad-pink: #e8527f;
    --ad-orange: #f29b32;
    --ad-grey: #ececec;
    --bank-blue: #1c3f8c;
    --logo-orange: #f28c1e;
    --logo-blue: #234d9c;
  }
  * { box-sizing: border-box; margin: 0; padding: 0; }
  html, body { width: 1200px; height: 667px; overflow: hidden; background: #ffffff; }
  body { position: relative; font-family: "Arimo", Arial, sans-serif; color: var(--ink); }

  .login { position: absolute; left: 960px; top: 12px; display: flex; align-items: center; gap: 8px; font-size: 13px; font-weight: 700; }
  .login svg { width: 22px; height: 22px; }

  .brand { position: absolute; left: 204px; top: 44px; display: flex; align-items: center; gap: 12px; }
  .brand-mark { width: 34px; height: 34px; background: var(--logo-orange); }
  .brand-name { font-size: 34px; font-weight: 700; color: var(--logo-blue); }

  .promo-banner { position: absolute; left: 612px; top: 52px; width: 492px; height: 60px; border: 1px solid var(--rule); background: #fff; text-align: center; padding-top: 6px; }
  .promo-banner .line-a { font-size: 24px; font-weight: 700; color: var(--ad-red); font-family: Georgia, serif; }
  .promo-banner .line-b { font-size: 15px; font-weight: 700; color: var(--ink); font-family: Georgia, serif; }

  .main-nav { position: absolute; left: 144px; top: 132px; width: 960px; height: 36px; border-top: 1px solid var(--rule); border-bottom: 1px solid var(--rule); }
  .main-nav a { position: absolute; top: 9px; font-size: 13px; font-weight: 700; color: var(--ink); text-decoration: none; white-space: nowrap; }

  .search-panel { position: absolute; left: 144px; top: 187px; width: 677px; height: 389px; border: 2px solid var(--panel-border); border-radius: 4px; box-shadow: 0 0 6px rgba(0,0,0,0.08); }
  .search-title { position: absolute; left: 24px; top: 44px; font-size: 29px; font-weight: 700; letter-spacing: -0.3px; }
  .select { position: absolute; width: 192px; height: 27px; background: var(--field-bg); border: 1px solid #a9a9a9; border-radius: 2px; color: var(--field-text); font-size: 11px; padding: 6px 8px; }
  .select::after { content: ""; position: absolute; right: 0; top: 0; width: 20px; height: 25px; background: #9d9d9d; }
  .select svg { position: absolute; right: 5px; top: 9px; width: 10px; height: 8px; z-index: 1; }
  .terms-note { position: absolute; left: 0; width: 100%; top: 255px; text-align: center; font-size: 10.5px; color: #444; }
  .terms-note a { color: var(--link-blue); font-weight: 700; text-decoration: none; }
  .search-button { position: absolute; left: 216px; top: 280px; width: 240px; height: 41px; background: var(--button-bg); border: 2px solid var(--button-border); border-radius: 3px; color: var(--button-text); font-family: inherit; font-size: 15px; box-shadow: inset 0 0 0 3px #eaf6fc; }

  .ad-slot { position: absolute; left: 835px; width: 226px; border: 1px solid var(--rule); }
  .ad-events { top: 187px; height: 185px; background: linear-gradient(160deg, var(--ad-orange), var(--ad-pink) 55%, #c93a73); }
  .ad-bank { top: 391px; height: 185px; background: linear-gradient(180deg, var(--ad-grey) 0%, #f6f6f6 55%, #d8dde9 70%, var(--bank-blue) 100%); }

  .footer-rule { position: absolute; left: 144px; top: 595px; width: 960px; border-top: 1px solid var(--rule); }
  .footer-links { position: absolute; left: 168px; top: 607px; display: flex; gap: 28px; font-size: 12px; font-weight: 700; }
  .footer-links a { color: var(--ink); text-decoration: none; }
  .copyright { position: absolute; left: 168px; top: 636px; font-size: 11px; color: var(--muted); }
  .social { position: absolute; left: 964px; top: 608px; display: flex; gap: 9px; }
  .social span { width: 30px; height: 30px; border-radius: 50%; }
  .social .s1 { background: #5fb8e6; }
  .social .s2 { background: #3f5d9c; }
  .social .s3 { background: #2c86bd; }
  .social .s4 { background: #f27a22; }
</style>
</head>
<body>
  <div class="login">
    <svg viewBox="0 0 22 22" aria-hidden="true"><circle cx="11" cy="11" r="10" fill="none" stroke="#111" stroke-width="1.6"/><rect x="7" y="10" width="8" height="6" fill="#111"/><path d="M8.5 10V8a2.5 2.5 0 0 1 5 0v2" fill="none" stroke="#111" stroke-width="1.6"/></svg>
    LOGIN
  </div>

  <div class="brand">
    <span class="brand-mark"></span>
    <span class="brand-name">BitLocate.ie</span>
  </div>

  <div class="promo-banner">
    <div class="line-a">Act Now! Buy the ebook.</div>
    <div class="line-b">Stop Losing $$$ and Get an Explosion of Traffic!</div>
  </div>

  <nav class="main-nav">
    <a style="left:17px">Parts Search</a>
    <a style="left:139px">Parts Request</a>
    <a style="left:264px">Damaged Repairables</a>
    <a style="left:446px">About</a>
    <a style="left:528px">Contact</a>
    <a style="left:624px">Dismantlers by Map</a>
    <a style="left:780px">Dismantlers by List</a>
  </nav>

  <section class="search-panel">
    <h1 class="search-title">Car Dismantlers - Car Parts Search</h1>
    <div class="select" style="left:22px;top:104px">Car Make<svg viewBox="0 0 10 8"><path d="M0 0h10L5 8z" fill="#fff"/></svg></div>
    <div class="select" style="left:245px;top:104px">Car Model<svg viewBox="0 0 10 8"><path d="M0 0h10L5 8z" fill="#fff"/></svg></div>
    <div class="select" style="left:461px;top:104px">Any Year<svg viewBox="0 0 10 8"><path d="M0 0h10L5 8z" fill="#fff"/></svg></div>
    <div class="select" style="left:22px;top:161px">Any Category<svg viewBox="0 0 10 8"><path d="M0 0h10L5 8z" fill="#fff"/></svg></div>
    <div class="select" style="left:245px;top:161px">Any Parts<svg viewBox="0 0 10 8"><path d="M0 0h10L5 8z" fill="#fff"/></svg></div>
    <p class="terms-note">By Clicking the search button below you are agreeing with the <a>Terms &amp; Conditions</a></p>
    <button class="search-button">Search Car Dismantlers</button>
  </section>

  <div class="ad-slot ad-events" role="img" aria-label="Advertisement: Midtown Quarter Evenings summer event poster with cocktail imagery"></div>
  <div class="ad-slot ad-bank" role="img" aria-label="Advertisement: Galleries Free Pass offer from Harbor Crest Bank with a card illustration"></div>

  <div class="footer-rule"></div>
  <div class="footer-links"><a>Home</a><a>About Us</a><a>Contact</a></div>
  <p class="copyright">© 2008-2011 www.bitlocate.ie - Car Dismantlers &amp; Car Breakers Search for Ireland</p>
  <div class="social" aria-label="Social links"><span class="s1"></span><span class="s2"></span><span class="s3"></span><span class="s4"></span></div>
</body>
</html>
```